Professional/modern business card design for construction company

We need a new business card design, double sided keeping it modern, sleek, professional and simple. We are an earthmoving business but do not want any pictures of machinery. I would like one side to have the logo and the other to have all the information, keeping with the colors in our logo. The business card will need to be able to be customised so we can use it for several different managers., we would also like to be able to use the design to apply it to other stationary ie. letterheads, notebooks etc. We do not really have a tag line but we could put on there that we specialise in - Agriculture, Civil Construction and Mining.

Contact Information for Business Card

Brolga Ridge Excavations Pty Ltd
ABN 58 402 937 615
82 Gumleaf Creek Road, Moree NSW 2400

Harold Benton
Managing Director
P 0418 639 204
E haroldbenton@brolgaridgeexc.com.au

Font styles to use
Serif
Sans Serif

Requirements
Nice to have
• I have attached some examples of ideas.
Should not have
• images of machinery

```html
<!DOCTYPE html>
<html lang="en">
<head>
<meta charset="utf-8">
<title>Brolga Ridge Excavations – Business Card</title>
<link rel="stylesheet" href="https://fonts.googleapis.com/css2?family=Open+Sans:wght@400;600;700&display=swap">
<style>
  :root {
    --backdrop: #262626;
    --card-white: #ffffff;
    --card-charcoal: #454545;
    --ink-dark: #404040;
    --ink-text: #4a4a4a;
    --accent-orange: #f28a1b;
    --band-grey: #454545;
    --paper-white: #ffffff;
  }
  * { margin: 0; padding: 0; box-sizing: border-box; }
  html, body {
    width: 1200px;
    height: 960px;
    overflow: hidden;
    background: var(--backdrop);
    font-family: "Open Sans", Arial, sans-serif;
  }
  .canvas { position: relative; width: 1200px; height: 960px; }

  .card {
    position: absolute;
    left: 261px;
    width: 679px;
    height: 387px;
  }
  .card--front { top: 61px; background: var(--card-white); }
  .card--back { top: 511px; background: var(--card-charcoal); }

  /* Front: brand name block */
  .brand-name {
    position: absolute;
    display: flex;
    align-items: center;
    gap: 14px;
  }
  .card--front .brand-name { left: 49px; top: 50px; }
  .brand-mark {
    width: 34px;
    height: 34px;
    background: var(--accent-orange);
    flex: none;
  }
  .brand-text {
    font-weight: 700;
    text-transform: uppercase;
    line-height: 1.05;
    letter-spacing: 0.5px;
  }
  .card--front .brand-text { color: var(--ink-dark); font-size: 27px; }

  /* Front: contact details */
  .contact {
    position: absolute;
    left: 48px;
    top: 176px;
    color: var(--ink-text);
    font-size: 16.5px;
    line-height: 22px;
  }
  .contact__address { margin-bottom: 6px; }
  .contact__row { display: flex; align-items: center; gap: 7px; }
  .contact__icon { width: 16px; height: 16px; flex: none; }
  .contact__abn { margin-top: 6px; }

  /* Front: name band */
  .name-band {
    position: absolute;
    right: 0;
    top: 224px;
    width: 281px;
    height: 69px;
  }
  .name-band__shape { position: absolute; inset: 0; }
  .name-band__text {
    position: absolute;
    right: 47px;
    top: 8px;
    text-align: right;
  }
  .person-name {
    color: var(--accent-orange);
    font-weight: 700;
    font-size: 23px;
    line-height: 30px;
    text-transform: uppercase;
  }
  .person-title {
    color: var(--paper-white);
    font-size: 17.5px;
    line-height: 24px;
  }

  /* Back */
  .card--back .brand-name {
    left: 0;
    right: 0;
    top: 118px;
    justify-content: center;
  }
  .card--back .brand-text {
    color: var(--paper-white);
    font-size: 36px;
    text-align: left;
  }
  .tagline {
    position: absolute;
    left: 0;
    right: 0;
    top: 294px;
    text-align: center;
    color: var(--paper-white);
    font-size: 16.5px;
    line-height: 23px;
  }
</style>
</head>
<body>
<main class="canvas">

  <section class="card card--front" aria-label="Business card front">
    <div class="brand-name">
      <span class="brand-mark"></span>
      <span class="brand-text">Brolga Ridge<br>Excavations Pty Ltd</span>
    </div>

    <div class="contact">
      <p class="contact__address">Brolga Ridge Excavations Pty Ltd<br>82 Gumleaf Creek Road<br>Moree NSW 2400</p>
      <p class="contact__row">
        <svg class="contact__icon" viewBox="0 0 16 16" aria-hidden="true"><path fill="#f28a1b" d="M2 5c0-2 2-3 6-3s6 1 6 3v1h-3V4.5H5V6H2zM4 7h8l2 7H2zm4 1.5a2 2 0 1 0 0 4 2 2 0 0 0 0-4z"/></svg>
        0418 639 204
      </p>
      <p class="contact__row">
        <svg class="contact__icon" viewBox="0 0 16 16" aria-hidden="true"><path fill="#f28a1b" d="M1 4h14v9H1zm1 1v.4l6 4 6-4V5z"/></svg>
        haroldbenton@brolgaridgeexc.com.au
      </p>
      <p class="contact__row">
        <svg class="contact__icon" viewBox="0 0 16 16" aria-hidden="true"><circle cx="8" cy="8" r="7" fill="#f28a1b"/><path fill="#fff" d="M5 4l3 1 1 3-2 1 1 3-3-2-1-3z"/></svg>
        www.brolgaridgeexc.com.au
      </p>
      <p class="contact__abn">ABN 58 402 937 615</p>
    </div>

    <div class="name-band">
      <svg class="name-band__shape" viewBox="0 0 281 69" preserveAspectRatio="none" aria-hidden="true">
        <polygon points="13,0 281,0 281,69 0,69" fill="#454545"/>
      </svg>
      <div class="name-band__text">
        <p class="person-name">Harold Benton</p>
        <p class="person-title">Managing Director</p>
      </div>
    </div>
  </section>

  <section class="card card--back" aria-label="Business card back">
    <div class="brand-name">
      <span class="brand-text">Brolga Ridge<br>Excavations Pty Ltd</span>
    </div>
    <p class="tagline">We specialise in<br>Agriculture, Civil Construction &amp; Mining.</p>
  </section>

</main>
</body>
</html>
```